Flyer for a company who uses pure argan oil

so we need a folder of 4 pages. including front & back.
unfolded format:
10cm wide by 6.5cm high.

Front card - as background use picture file 'front'
in the lower feathers in these languages ​​'thank you'
Thank you Bedankt Merci Danke
Shukran Grazie Tak Kop khun
Arigatô Hvala Dankie Mahalo
Please use a suitable font as on the bottle.

Back of card - as background use picture file 'back'
again in the lower springs
'Yes Vasko is here'

Inside of the folding card fitting and soft pink background.

With the following text:
Wist u dat het Vasko team alles zelf doet, van de noot tot in het flesje.
Met Vasko koopt u een 100% puur natuurproduct: volledig vrij van toevoegingen en bewaarmiddelen.
U geeft uw huid, haar, nagels de allerbeste verzorging, op elk moment van de dag!
Psoriasis, droge huid, eczeem, anti aging en zoveel meer voor heel het gezin.

''Translations of the text in English so you can understand it''
Did you know that the Vasko team does everything itself, from the nut to the bottle. With Vasko you buy a 100% pure natural product: completely free of additives and preservatives. You give your skin, hair and nails the very best care, at any time of the day! Psoriasis, dry skin, eczema, anti-aging and so much more for the whole family.

A new text with the title 'PURE HEILZAAMHEID IN ÉÉN TOPPRODUCT '
And then these 3 benefits under the title.
● Een allesomvattende dag- en nachtverzorging

● Hydraterende en egaliserende eigenschappen

● Herstellend bij huid-, haar- en nagel kwaaltjes

And then somewhere else maybe in a banner or green circle
Vegan - niet getest op dieren - 100% ongeraffineerde Argan olie

Vegan - not tested on animals - 100% unrefined Argan oil

Thanks!!

```html
<!DOCTYPE html>
<html lang="nl">
<head>
<meta charset="utf-8">
<title>Vasko – Pure Argan oil folder</title>
<link href="https://fonts.googleapis.com/css2?family=Cabin+Condensed:wght@400;500&family=Oswald:wght@300;400&family=Poppins:wght@400;500&display=swap" rel="stylesheet">
<style>
  :root {
    --page-bg: #e4e4e4;
    --band-brown: rgba(122, 70, 62, 0.93);
    --ink-brown: #8c4236;
    --accent-rust: #b4533f;
    --inside-left: #e8cbc8;
    --inside-right: #f6dddb;
    --feather-light: #f7ece9;
    --feather-pink: #e8b9ae;
    --white: #ffffff;
  }
  * { box-sizing: border-box; margin: 0; padding: 0; }
  html, body { width: 1200px; height: 571px; overflow: hidden; }
  body {
    background: var(--page-bg);
    position: relative;
    font-family: "Poppins", sans-serif;
  }
  .spread {
    position: absolute;
    top: 70px;
    width: 494px;
    height: 408px;
    display: flex;
  }
  .spread--outside { left: 55px; }
  .spread--inside { left: 622px; }
  .panel { position: relative; width: 247px; height: 100%; overflow: hidden; }

  /* Outside */
  .photo {
    position: absolute; inset: 0;
    background:
      radial-gradient(ellipse at 50% 38%, #c98a3a 0 14%, transparent 15%),
      radial-gradient(ellipse at 30% 95%, var(--feather-pink) 0, transparent 55%),
      radial-gradient(ellipse at 80% 10%, var(--feather-pink) 0, transparent 45%),
      linear-gradient(180deg, var(--feather-light), #f1dcd6 70%, #e9c3b9);
  }
  .photo--front {
    background:
      radial-gradient(ellipse at 52% 36%, #b9772e 0 13%, transparent 14%),
      radial-gradient(ellipse at 20% 90%, var(--feather-pink) 0, transparent 55%),
      radial-gradient(ellipse at 90% 20%, var(--feather-pink) 0, transparent 40%),
      linear-gradient(180deg, #efe6e4, #f0dad4 70%, #e6bcb1);
  }
  .band {
    position: absolute; left: 0; right: 0; top: 263px; height: 128px;
    background: var(--band-brown);
    color: var(--white);
    text-align: center;
  }
  .band__tagline {
    margin-top: 62px;
    font-family: "Poppins", sans-serif;
    font-size: 12.5px;
    letter-spacing: 1.6px;
  }
  .band__brand {
    margin-top: 8px;
    font-family: "Cabin Condensed", sans-serif;
    font-weight: 500;
    font-size: 38px;
    line-height: 1;
  }
  .band__product {
    font-family: "Cabin Condensed", sans-serif;
    font-size: 14px;
    margin-top: 2px;
  }
  .band__thanks {
    font-family: "Cabin Condensed", sans-serif;
    font-size: 14.5px;
    line-height: 16px;
    margin-top: 3px;
  }

  /* Inside */
  .panel--intro { background: var(--inside-left); color: var(--ink-brown); text-align: center; }
  .panel--benefits { background: var(--inside-right); color: var(--ink-brown); }
  .intro__lead {
    margin: 82px 10px 0;
    font-weight: 500;
    font-size: 13.5px;
    line-height: 18px;
  }
  .divider { display: block; margin: 6px auto 4px; }
  .intro__body {
    margin: 0 6px;
    font-size: 11.6px;
    line-height: 15.5px;
  }
  .intro__brand {
    margin-top: 30px;
    font-weight: 500;
    font-size: 38px;
    color: var(--accent-rust);
    line-height: 1;
  }
  .fold-line {
    position: absolute; left: 0; right: 0; top: 393px;
    height: 1.5px; background: var(--accent-rust);
  }
  .benefits__title {
    margin: 44px 6px 0 10px;
    font-family: "Oswald", sans-serif;
    font-weight: 400;
    font-size: 31px;
    line-height: 34px;
    letter-spacing: -0.3px;
    white-space: nowrap;
  }
  .benefits__subtitle {
    display: flex; align-items: center; gap: 6px;
    margin: 0 6px 0 10px;
    font-family: "Oswald", sans-serif;
    font-weight: 300;
    font-size: 14px;
    letter-spacing: 2.2px;
    white-space: nowrap;
  }
  .benefits__subtitle::before, .benefits__subtitle::after {
    content: ""; flex: 1; height: 1px; background: var(--ink-brown);
  }
  .benefit-list { list-style: none; margin-top: 18px; }
  .benefit {
    position: relative;
    height: 50px;
    margin: 0 10px 18px 34px;
    border: 1.2px dashed var(--accent-rust);
    border-left: none;
    border-radius: 0 22px 22px 0;
    display: flex; align-items: center;
    padding-left: 20px;
    font-size: 12px;
    line-height: 16px;
  }
  .benefit__icon {
    position: absolute; left: -24px; top: 4px;
    width: 42px; height: 42px;
    border: 1.4px solid var(--accent-rust);
    border-radius: 50%;
    background: var(--inside-right);
    display: flex; align-items: center; justify-content: center;
  }
  .seals { position: absolute; left: 62px; top: 346px; display: flex; gap: 16px; }
  .seal {
    width: 31px; height: 31px; border-radius: 50%;
    border: 1.5px solid var(--accent-rust);
  }
</style>
</head>
<body>

<section class="spread spread--outside" aria-label="Buitenzijde folder">
  <div class="panel panel--back">
    <div class="photo" role="img" aria-label="Productfoto: flesje arganolie tussen zachtroze veren"></div>
    <div class="band">
      <p class="band__tagline">Yes Vasko is here</p>
    </div>
  </div>
  <div class="panel panel--front">
    <div class="photo photo--front" role="img" aria-label="Productfoto: sprayfles arganolie tussen zachtroze veren"></div>
    <div class="band">
      <p class="band__brand">Vasko</p>
      <p class="band__product">Pure Argan oil</p>
      <p class="band__thanks">Thank you Bedankt Merci Danke<br>Shukran Grazie Tak Kop khun<br>Arigatô Hvala Dankie Mahalo</p>
    </div>
  </div>
</section>

<section class="spread spread--inside" aria-label="Binnenzijde folder">
  <div class="panel panel--intro">
    <p class="intro__lead">Wist u dat het Vasko team alles zelf doet, van de noot tot in het flesje. Met Vasko koopt u een 100% puur natuurproduct:</p>
    <svg class="divider" width="60" height="8" viewBox="0 0 60 8" aria-hidden="true">
      <line x1="0" y1="4" x2="24" y2="4" stroke="#8c4236" stroke-width="1"/>
      <circle cx="30" cy="4" r="2.5" fill="#8c4236"/>
      <line x1="36" y1="4" x2="60" y2="4" stroke="#8c4236" stroke-width="1"/>
    </svg>
    <p class="intro__body">volledig vrij van toevoegingen en bewaarmiddelen.<br>U geeft uw huid, haar, nagels de allerbeste verzorging, op elk moment van de dag! Psoriasis, droge huid, eczeem, anti aging en zoveel meer voor heel het gezin.</p>
    <p class="intro__brand">Vasko</p>
    <div class="fold-line"></div>
  </div>

  <div class="panel panel--benefits">
    <h1 class="benefits__title">PURE HEILZAAMHEID</h1>
    <p class="benefits__subtitle">IN ÉÉN TOPPRODUCT</p>
    <ul class="benefit-list">
      <li class="benefit">
        <span class="benefit__icon">
          <svg width="24" height="24" viewBox="0 0 24 24" fill="none" stroke="#b4533f" stroke-width="1.2" aria-hidden="true">
            <circle cx="8" cy="9" r="3"/>
            <path d="M8 3v1.5M8 13.5V15M2 9h1.5M12.5 9H14M3.8 4.8l1 1M11.2 4.8l-1 1"/>
            <path d="M18 12a4.5 4.5 0 1 0 2 6 3.6 3.6 0 0 1-2-6z"/>
            <line x1="4" y1="21" x2="20" y2="3"/>
          </svg>
        </span>
        Een allesomvattende dag- en nachtverzorging
      </li>
      <li class="benefit">
        <span class="benefit__icon">
          <svg width="24" height="24" viewBox="0 0 24 24" fill="none" stroke="#b4533f" stroke-width="1.2" aria-hidden="true">
            <path d="M9 4c-3 5-5 8-5 11a5 5 0 0 0 10 0c0-3-2-6-5-11z"/>
            <path d="M17 10c-2 3-3 5-3 6.5a3 3 0 0 0 6 0c0-1.5-1-3.5-3-6.5z"/>
          </svg>
        </span>
        Hydraterende en egaliserende eigenschappen
      </li>
      <li class="benefit">
        <span class="benefit__icon">
          <svg width="24" height="24" viewBox="0 0 24 24" fill="none" stroke="#b4533f" stroke-width="1.2" aria-hidden="true">
            <path d="M3 14h6M15 14h6"/>
            <path d="M9 14c0 4 1.5 6 3 6s3-2 3-6"/>
            <path d="M12 18c0-5 0-9 1.5-14"/>
          </svg>
        </span>
        Herstellend bij huid-, haar- en nagel kwaaltjes
      </li>
    </ul>
    <div class="seals" aria-label="Vegan, niet getest op dieren, 100% ongeraffineerde arganolie">
      <span class="seal"></span>
      <span class="seal"></span>
      <span class="seal"></span>
    </div>
    <div class="fold-line"></div>
  </div>
</section>

</body>
</html>
```